Need a webinar banner promo to place on social media

We are organise a series of webinars in coming months.

We need a webinar banner design to be posted on Facebook and linkedin. The banner is for our webinar titled: Steps to Unveil your venture with poise and polish.

our website is www.bravolinhub.com.au

there is a link on the website to the webinar registration for your reference.

```html
<!DOCTYPE html>
<html lang="en">
<head>
<meta charset="utf-8">
<title>Webinar Banners – Bravolin Hub</title>
<link href="https://fonts.googleapis.com/css2?family=Montserrat:wght@400;600;700;800&family=Arimo:wght@700&display=swap" rel="stylesheet">
<style>
  :root {
    --navy-deep: #071a5e;
    --navy: #0a2a80;
    --navy-light: #123c9c;
    --gold-dark: #a8791c;
    --gold: #d4ab45;
    --gold-light: #f0d480;
    --yellow: #f2e274;
    --bronze: #c08a2a;
    --ring: #3b5fb0;
    --white: #ffffff;
    --label: #333333;
    --page: #e2e2e2;
  }
  * { margin: 0; padding: 0; box-sizing: border-box; }
  html, body { width: 1200px; height: 1200px; overflow: hidden; }
  body {
    background: radial-gradient(circle at 50% 60%, #eeeeee 0%, var(--page) 60%, #d6d6d6 100%);
    font-family: "Montserrat", sans-serif;
    position: relative;
  }

  .banner {
    position: absolute;
    overflow: hidden;
    background:
      linear-gradient(125deg, transparent 0 38%, rgba(255,255,255,0.04) 38% 52%, transparent 52%),
      linear-gradient(160deg, var(--navy-light) 0%, var(--navy) 40%, var(--navy-deep) 100%);
    box-shadow: 0 14px 22px rgba(0,0,0,0.35);
  }
  .banner--linkedin { left: 118px; top: 250px; width: 964px; height: 315px; }
  .banner--facebook { left: 299px; top: 643px; width: 586px; height: 255px; }

  .banner__decor { position: absolute; inset: 0; width: 100%; height: 100%; }
  .banner > * { position: absolute; }

  .dot-grid { background: rgba(255,255,255,0.16); border-radius: 2px; }

  .headline {
    font-weight: 800;
    line-height: 1;
    letter-spacing: -1px;
    background: linear-gradient(180deg, var(--gold-light) 0%, var(--gold) 45%, var(--gold-dark) 100%);
    -webkit-background-clip: text;
    background-clip: text;
    color: transparent;
  }
  .title {
    color: var(--white);
    font-weight: 700;
    line-height: 1.3;
    white-space: nowrap;
  }
  .title__slashes { display: inline-block; vertical-align: middle; margin-left: 4px; }

  .register {
    display: flex;
    align-items: center;
    background: var(--white);
    border-radius: 999px;
    overflow: hidden;
  }
  .register__cta {
    height: 100%;
    display: flex;
    align-items: center;
    justify-content: center;
    background: linear-gradient(90deg, var(--gold-dark), var(--gold) 50%, var(--gold-light));
    color: var(--navy-deep);
    font-weight: 700;
    border-radius: 999px;
    white-space: nowrap;
  }
  .register__url { color: #1a1a2e; font-weight: 400; white-space: nowrap; }
  .register__url b { font-weight: 700; }

  .date__bracket {
    position: absolute; top: 0; bottom: 0;
    border: 2px solid var(--white);
  }
  .date__bracket--left { left: 0; border-right: none; }
  .date__bracket--right { right: 0; border-left: none; }
  .date__day { position: absolute; font-weight: 800; line-height: 1; letter-spacing: -0.08em; }
  .date__suffix, .date__month, .date__time { position: absolute; color: var(--white); font-weight: 700; line-height: 1; white-space: nowrap; }
  .date__year { position: absolute; font-weight: 800; line-height: 1; }

  .brand {
    color: var(--gold);
    font-weight: 700;
    line-height: 1.05;
    text-align: center;
    letter-spacing: 0.5px;
  }

  /* LinkedIn */
  .banner--linkedin .dot-grid--a { left: 42px; top: 34px; width: 28px; height: 28px; }
  .banner--linkedin .dot-grid--b { left: 680px; top: 22px; width: 92px; height: 26px; }
  .banner--linkedin .dot-grid--c { left: 768px; top: 262px; width: 20px; height: 20px; }
  .banner--linkedin .headline { left: 44px; top: 66px; font-size: 76px; }
  .banner--linkedin .title { left: 56px; top: 134px; font-size: 25px; }
  .banner--linkedin .register { left: 51px; top: 244px; width: 538px; height: 36px; }
  .banner--linkedin .register__cta { width: 152px; font-size: 14.5px; }
  .banner--linkedin .register__url { margin-left: 16px; font-size: 18px; }
  .banner--linkedin .date { left: 478px; top: 73px; width: 218px; height: 122px; }
  .banner--linkedin .date__bracket { width: 22px; }
  .banner--linkedin .date__day { left: 24px; top: 10px; font-size: 92px; }
  .banner--linkedin .date__suffix { left: 115px; top: 13px; font-size: 20px; }
  .banner--linkedin .date__month { left: 116px; top: 37px; font-size: 20px; }
  .banner--linkedin .date__year { left: 115px; top: 57px; font-size: 30px; }
  .banner--linkedin .date__time { left: 34px; top: 88px; font-size: 22px; }
  .banner--linkedin .brand { left: 618px; top: 226px; width: 130px; font-size: 22px; }

  /* Facebook */
  .banner--facebook .dot-grid--a { left: 18px; top: 27px; width: 28px; height: 28px; }
  .banner--facebook .dot-grid--b { left: 367px; top: 27px; width: 96px; height: 26px; }
  .banner--facebook .dot-grid--c { left: 410px; top: 214px; width: 18px; height: 18px; }
  .banner--facebook .brand { left: 30px; top: 30px; width: 118px; font-size: 19px; }
  .banner--facebook .headline { left: 26px; top: 96px; font-size: 44px; }
  .banner--facebook .title { left: 32px; top: 138px; font-size: 14px; }
  .banner--facebook .register { left: 25px; top: 206px; width: 378px; height: 26px; }
  .banner--facebook .register__cta { width: 108px; font-size: 10.5px; }
  .banner--facebook .register__url { margin-left: 12px; font-size: 13px; }
  .banner--facebook .date { left: 274px; top: 99px; width: 126px; height: 70px; }
  .banner--facebook .date__bracket { width: 13px; }
  .banner--facebook .date__day { left: 13px; top: 6px; font-size: 54px; }
  .banner--facebook .date__suffix { left: 67px; top: 7px; font-size: 11px; }
  .banner--facebook .date__month { left: 68px; top: 19px; font-size: 12px; }
  .banner--facebook .date__year { left: 67px; top: 31px; font-size: 17px; }
  .banner--facebook .date__time { left: 19px; top: 53px; font-size: 13px; }

  .caption {
    position: absolute;
    left: 0; width: 1200px;
    text-align: center;
    font-family: "Arimo", sans-serif;
    font-weight: 700;
    font-size: 28px;
    color: var(--label);
  }
  .caption--linkedin { top: 590px; }
  .caption--facebook { top: 922px; left: -8px; }
</style>
</head>
<body>

  <section class="banner banner--linkedin" aria-label="LinkedIn webinar banner">
    <svg class="banner__decor" viewBox="0 0 964 315" aria-hidden="true">
      <defs>
        <linearGradient id="speaker-photo" x1="0" y1="0" x2="1" y2="1">
          <stop offset="0" stop-color="#2a3560"/>
          <stop offset="0.55" stop-color="#5a4630"/>
          <stop offset="1" stop-color="#1a1a22"/>
        </linearGradient>
      </defs>
      <circle cx="914" cy="154" r="148" fill="none" stroke="#fff" stroke-width="2.5"/>
      <circle cx="900" cy="152" r="146" fill="var(--yellow)"/>
      <circle cx="846" cy="154" r="93" fill="var(--ring)" opacity="0.85"/>
      <circle cx="888" cy="29" r="18" fill="var(--bronze)"/>
      <circle cx="924" cy="296" r="9" fill="#fff"/>
      <circle cx="806" cy="250" r="10" fill="none" stroke="var(--yellow)" stroke-width="2"/>
    </svg>
    <svg style="left:763px;top:71px;width:166px;height:166px" viewBox="0 0 166 166" role="img" aria-label="Photo of a speaker at a lectern addressing a seated audience">
      <circle cx="83" cy="83" r="83" fill="url(#speaker-photo)"/>
    </svg>
    <div class="dot-grid dot-grid--a" role="img" aria-label="Dot grid accent"></div>
    <div class="dot-grid dot-grid--b" role="img" aria-label="Dot grid accent"></div>
    <div class="dot-grid dot-grid--c" role="img" aria-label="Dot grid accent"></div>

    <h1 class="headline">WEBINAR</h1>
    <p class="title">Steps to Unveil your Venture<br>with Poise and Polish<svg class="title__slashes" width="90" height="16" viewBox="0 0 90 16" aria-hidden="true">
        <g stroke="#fff" stroke-width="1.6">
          <line x1="3" y1="15" x2="8" y2="1"/><line x1="13" y1="15" x2="18" y2="1"/><line x1="23" y1="15" x2="28" y2="1"/><line x1="33" y1="15" x2="38" y2="1"/><line x1="43" y1="15" x2="48" y2="1"/><line x1="53" y1="15" x2="58" y2="1"/><line x1="63" y1="15" x2="68" y2="1"/><line x1="73" y1="15" x2="78" y2="1"/><line x1="83" y1="15" x2="88" y2="1"/>
        </g>
      </svg></p>

    <div class="date">
      <span class="date__bracket date__bracket--left"></span>
      <span class="date__bracket date__bracket--right"></span>
      <span class="date__day headline">15</span>
      <span class="date__suffix">TH</span>
      <span class="date__month">MARCH</span>
      <span class="date__year headline">2023</span>
      <span class="date__time">7:00 pm AEDT</span>
    </div>

    <div class="brand">BRAVOLIN<br>HUB</div>

    <div class="register">
      <span class="register__cta">REGISTER NOW</span>
      <span class="register__url">www.<b>bravolinhub</b>.com.au/webinars</span>
    </div>
  </section>
  <p class="caption caption--linkedin">Linkedin Banner</p>

  <section class="banner banner--facebook" aria-label="Facebook webinar banner">
    <svg class="banner__decor" viewBox="0 0 586 255" aria-hidden="true">
      <circle cx="585" cy="129" r="122" fill="none" stroke="#fff" stroke-width="2"/>
      <circle cx="565" cy="129" r="108" fill="var(--yellow)"/>
      <circle cx="485" cy="129" r="74" fill="var(--ring)" opacity="0.85"/>
      <circle cx="519" cy="27" r="14" fill="var(--bronze)"/>
      <circle cx="547" cy="243" r="7" fill="#fff"/>
      <circle cx="440" cy="206" r="9" fill="none" stroke="var(--yellow)" stroke-width="2"/>
    </svg>
    <svg style="left:419px;top:63px;width:132px;height:132px" viewBox="0 0 132 132" role="img" aria-label="Photo of a speaker at a lectern addressing a seated audience">
      <circle cx="66" cy="66" r="66" fill="url(#speaker-photo)"/>
    </svg>
    <div class="dot-grid dot-grid--a" role="img" aria-label="Dot grid accent"></div>
    <div class="dot-grid dot-grid--b" role="img" aria-label="Dot grid accent"></div>
    <div class="dot-grid dot-grid--c" role="img" aria-label="Dot grid accent"></div>

    <div class="brand">BRAVOLIN<br>HUB</div>

    <h2 class="headline">WEBINAR</h2>
    <p class="title">Steps to Unveil your Venture<br>with Poise and Polish<svg class="title__slashes" width="58" height="10" viewBox="0 0 58 10" aria-hidden="true">
        <g stroke="#fff" stroke-width="1.2">
          <line x1="2" y1="9" x2="5" y2="1"/><line x1="9" y1="9" x2="12" y2="1"/><line x1="16" y1="9" x2="19" y2="1"/><line x1="23" y1="9" x2="26" y2="1"/><line x1="30" y1="9" x2="33" y2="1"/><line x1="37" y1="9" x2="40" y2="1"/><line x1="44" y1="9" x2="47" y2="1"/><line x1="51" y1="9" x2="54" y2="1"/>
        </g>
      </svg></p>

    <div class="date">
      <span class="date__bracket date__bracket--left"></span>
      <span class="date__bracket date__bracket--right"></span>
      <span class="date__day headline">15</span>
      <span class="date__suffix">TH</span>
      <span class="date__month">MARCH</span>
      <span class="date__year headline">2023</span>
      <span class="date__time">7:00 pm AEDT</span>
    </div>

    <div class="register">
      <span class="register__cta">REGISTER NOW</span>
      <span class="register__url">www.<b>bravolinhub</b>.com.au/webinars</span>
    </div>
  </section>
  <p class="caption caption--facebook">Facebook Banner</p>

</body>
</html>
```